Brell Harbor Company Business Cards

Front and Back Business Card - logo and text setup - cool design. I need workable photoshop or illustrator files so I can setup each employee card with design that is created
Updates

Hi everyone, thank you for the great entries. Please no more white and blue cards - there are so many already - black and silver only now please. thanks!

Target Market(s)

Construction Industry - Facility Managers

Industry/Entity Type

Construction

Contact Information for Business Card

I really like contemporary simplistic looks - clean neat....not opposed to seeing some black backrounds

Requirements
Must have
• Logo/website address with design on front only - www.brellharbor-example.com (logo attached)
• Back:
• Name/Title/Company Address/Phone/email address
Nice to have
• Cool design
Should not have
• Nothing gimmicky like Fire or Water - since we are a Fire Protection company - it has all been done

```html
<!DOCTYPE html>
<html lang="en">
<head>
<meta charset="utf-8">
<title>Brell Harbor Company Business Cards</title>
<link href="https://fonts.googleapis.com/css2?family=Lato:wght@400;700;900&display=swap" rel="stylesheet">
<style>
  :root {
    --backdrop: #7b7b7b;
    --card-dark: #050505;
    --card-mid: #1a1a1a;
    --silver-light: #d9dcdf;
    --silver: #b4b8bd;
    --silver-dim: #8a8f95;
  }
  * { margin: 0; padding: 0; box-sizing: border-box; }
  html, body { width: 1200px; height: 900px; overflow: hidden; }
  body {
    background: var(--backdrop);
    font-family: "Lato", sans-serif;
    display: flex;
    align-items: center;
    justify-content: center;
    gap: 50px;
  }
  .card {
    position: relative;
    width: 525px;
    height: 300px;
    background: linear-gradient(135deg, var(--card-mid) 0%, var(--card-dark) 55%);
    box-shadow: 0 14px 30px rgba(0,0,0,0.45);
    border-radius: 3px;
  }
  .brand {
    display: flex;
    align-items: center;
    gap: 10px;
  }
  .brand-mark {
    width: 16px;
    height: 16px;
    background: var(--silver);
  }
  .brand-name {
    font-weight: 900;
    font-size: 40px;
    color: var(--silver-light);
    letter-spacing: -0.5px;
    line-height: 1;
    white-space: nowrap;
  }
  /* back: contact side */
  .card-back .brand { position: absolute; top: 50px; left: 140px; }
  .card-back .brand-name { font-size: 36px; }
  .person {
    position: absolute;
    top: 150px;
    left: 40px;
    width: 198px;
    text-align: right;
  }
  .person-name {
    font-size: 24px;
    font-weight: 700;
    color: var(--silver-light);
    white-space: nowrap;
  }
  .person-title {
    font-size: 15px;
    color: var(--silver);
    margin-top: 2px;
  }
  .divider {
    position: absolute;
    left: 258px;
    top: 140px;
    width: 2px;
    height: 110px;
    background: var(--silver-dim);
  }
  .contact-list {
    position: absolute;
    left: 280px;
    top: 140px;
    list-style: none;
    color: var(--silver);
    font-size: 14px;
    line-height: 1.35;
  }
  .contact-list li {
    display: flex;
    align-items: flex-start;
    gap: 8px;
    margin-bottom: 6px;
    white-space: nowrap;
  }
  .contact-list svg { width: 13px; height: 13px; margin-top: 3px; flex: none; fill: var(--silver-dim); }
  /* front: logo side */
  .card-front {
    display: flex;
    flex-direction: column;
    align-items: center;
    justify-content: center;
    gap: 16px;
  }
  .website {
    font-size: 15px;
    letter-spacing: 4px;
    color: var(--silver);
    white-space: nowrap;
  }
</style>
</head>
<body>
  <section class="card card-back" aria-label="Card back with contact details">
    <div class="brand">
      <span class="brand-mark"></span>
      <span class="brand-name">Brell Harbor</span>
    </div>
    <div class="person">
      <p class="person-name">Dana Whitlock</p>
      <p class="person-title">Founder</p>
    </div>
    <div class="divider"></div>
    <ul class="contact-list">
      <li>
        <svg viewBox="0 0 24 24"><path d="M6.6 10.8a15 15 0 0 0 6.6 6.6l2.2-2.2c.3-.3.7-.4 1-.2 1.1.4 2.3.6 3.6.6.6 0 1 .4 1 1V20c0 .6-.4 1-1 1A17 17 0 0 1 3 4c0-.6.4-1 1-1h3.5c.6 0 1 .4 1 1 0 1.3.2 2.5.6 3.6.1.3 0 .7-.2 1z"/></svg>
        <span>000-000-000</span>
      </li>
      <li>
        <svg viewBox="0 0 24 24"><path d="M2 5h20v14H2z M2 5l10 8 10-8" fill="none" stroke="#8a8f95" stroke-width="2.5"/></svg>
        <span>info@brellharbor-example.com</span>
      </li>
      <li>
        <svg viewBox="0 0 24 24"><path d="M12 2a7 7 0 0 0-7 7c0 5 7 13 7 13s7-8 7-13a7 7 0 0 0-7-7zm0 9.5a2.5 2.5 0 1 1 0-5 2.5 2.5 0 0 1 0 5z"/></svg>
        <span>42 Linden Avenue<br>Kestrel Point, ST 00000</span>
      </li>
    </ul>
  </section>

  <section class="card card-front" aria-label="Card front with company name and website">
    <div class="brand">
      <span class="brand-mark"></span>
      <span class="brand-name">Brell Harbor</span>
    </div>
    <p class="website">www.brellharbor-example.com</p>
  </section>
</body>
</html>
```